Brochure for a paper wholesaler who wants to educate his print industry clients

We will be making a stapled informative brochure, that contains basic information about our paper products - the types of paper there is, their characteristics and other useful information.
As we are part of a paper wholesaler group in Europe - ORVANTE, we received a brochure in German that has this kind of information. The text in it is not as important. What is important is the layout of the document and how the text will appear in it (added in the uploaded files - 210915_Wiessenswertes_TKLM_F51.pdf).
We are allowed to tinker with this file and adjust it to our needs. So there are also .idml and .indd files available (also in the uploaded files).
We would like to keep the custom page size of 210 x290mm (8.3x11.4 in), or you can go up to 210x297mm (8.3x11.7 in).
What we want is a modern looking design that contains our companies red bordo and white/ grey colours to replace the existing green colours in this borchure. The pictures and appearance of the file can be changed according to your views and what you think would look good. We don't necessarily want to keep the same design, we just want the layout of the document be the same, as we will be placing our translated text into it. The ORVANTE logo should be replaced with our own logo (KEMSU Logo.png).
As for how it could look, it could go together with our paper presentation, for which the design can be seen in the "KEMSU Base - v2.pptx".
Holiday season, so have a lot of tasks to take care of and not as much time to check PixelForge as often.

```html
<!DOCTYPE html>
<html lang="de">
<head>
<meta charset="utf-8">
<title>KEMSU – Wissenswert Broschüre</title>
<link href="https://fonts.googleapis.com/css2?family=Montserrat:wght@400;500;600;700;800&display=swap" rel="stylesheet">
<style>
  :root {
    --bordo: #7a2328;
    --bordo-deep: #6a1d22;
    --paper: #ffffff;
    --panel: #e9e9e9;
    --tile: #e4e4e4;
    --stage: #d6d6d6;
    --ink: #222222;
    --green: #1f6a47;
  }
  * { box-sizing: border-box; margin: 0; padding: 0; }
  html, body { width: 867px; height: 1200px; overflow: hidden; }
  body { background: var(--stage); font-family: "Montserrat", sans-serif; color: var(--ink); position: relative; }

  .spread { position: absolute; left: 13px; width: 840px; height: 580px; display: flex; box-shadow: 0 6px 18px rgba(0,0,0,.18); }
  .spread--cover { top: 13px; }
  .spread--inside { top: 607px; }
  .page { position: relative; width: 420px; height: 580px; overflow: hidden; background: var(--paper); }

  .brand { display: flex; align-items: center; gap: 7px; color: var(--bordo); font-weight: 600; letter-spacing: .38em; }
  .brand__mark { width: 14px; height: 14px; border: 2px solid var(--bordo); }

  /* back cover */
  .back__photo { position: absolute; right: 0; top: 28px; width: 190px; bottom: 0; background: linear-gradient(160deg, #f1f1f1, #c9c9c9 60%, #a9a39a); }
  .back__panel { position: absolute; left: 0; top: 0; width: 230px; height: 100%; background: var(--panel); }
  .back__contact { position: absolute; left: 0; top: 120px; width: 230px; display: flex; flex-direction: column; align-items: center; }
  .back__contact .brand { font-size: 14px; margin-bottom: 14px; }
  .icon-row { display: flex; gap: 8px; margin-bottom: 12px; }
  .icon-dot { width: 22px; height: 22px; border-radius: 50%; background: var(--bordo); display: flex; align-items: center; justify-content: center; }
  .contact-line { display: flex; align-items: center; gap: 6px; font-size: 10.5px; font-weight: 500; margin: 4px 0; }
  .contact-line::before, .contact-line::after { content: ""; width: 26px; border-top: 1px dotted var(--bordo); }
  .back__worker { position: absolute; left: 10px; bottom: 0; width: 220px; height: 200px; background: linear-gradient(180deg, #ececec, #c7d86a 55%, #b9b2a6); border-radius: 4px 4px 0 0; }

  /* front cover */
  .front__photo { position: absolute; inset: 0; background: linear-gradient(170deg, #f4f4f4 0%, #d8d8d8 45%, #bdbdbd 75%, #a8a090 100%); }
  .front__brand { position: absolute; top: 150px; right: 70px; font-size: 18px; }
  .front__band { position: absolute; left: 0; right: 0; top: 250px; height: 200px; background: var(--bordo); color: #fff; text-align: center; padding-top: 28px; }
  .front__title { font-size: 38px; font-weight: 800; letter-spacing: .02em; line-height: 1; }
  .front__topics { font-size: 16px; font-weight: 600; margin-top: 10px; line-height: 1.25; }
  .front__rule { width: 90px; border-top: 1px solid #fff; margin: 14px auto 10px; }
  .front__tagline { font-size: 10.5px; font-weight: 500; }
  .front__web { position: absolute; top: 480px; left: 0; right: 0; text-align: center; font-size: 15px; font-weight: 700; color: var(--ink); }

  /* inside left */
  .intro__photo { position: absolute; left: 0; right: 0; bottom: 0; height: 360px; background: linear-gradient(160deg, #8b6e5a, #c9b8a6 45%, #e0a96e 70%, #5f7fb0); }
  .intro__header { position: absolute; left: 0; top: 0; width: 420px; height: 300px; }
  .intro__text { position: absolute; left: 34px; top: 42px; width: 360px; color: #fff; }
  .intro__title { font-size: 27px; font-weight: 700; line-height: 1.15; letter-spacing: .02em; }
  .intro__rule { width: 260px; border-top: 1px solid rgba(255,255,255,.8); margin: 16px 0 12px; }
  .intro__sub { font-size: 15px; font-weight: 400; line-height: 1.3; }

  /* inside right */
  .glossary { position: absolute; inset: 28px 22px; display: grid; grid-template-columns: 1fr 1fr; grid-template-rows: repeat(4, 1fr); }
  .term { display: flex; flex-direction: column; align-items: center; justify-content: center; text-align: center; padding: 10px 16px; }
  .term--tile { background: var(--tile); }
  .term__icon { width: 30px; height: 26px; margin-bottom: 6px; }
  .term__name { color: var(--green); font-size: 9.5px; font-weight: 700; text-transform: uppercase; margin-bottom: 4px; line-height: 1.2; }
  .term__text { font-size: 7.5px; line-height: 1.35; }
  .term .brand { font-size: 15px; }
</style>
</head>
<body>

<section class="spread spread--cover">
  <div class="page page--back">
    <div class="back__photo" role="img" aria-label="Photo of a paper warehouse aisle with stacked pallets"></div>
    <div class="back__panel"></div>
    <div class="back__contact">
      <div class="brand"><span class="brand__mark"></span>KEMSU</div>
      <div class="icon-row">
        <span class="icon-dot"><svg width="12" height="12" viewBox="0 0 24 24" fill="none" stroke="#fff" stroke-width="2"><path d="M5 3h4l2 5-3 2a12 12 0 0 0 6 6l2-3 5 2v4a2 2 0 0 1-2 2A18 18 0 0 1 3 5a2 2 0 0 1 2-2z"/></svg></span>
        <span class="icon-dot"><svg width="12" height="12" viewBox="0 0 24 24" fill="none" stroke="#fff" stroke-width="2"><rect x="3" y="5" width="18" height="14"/><path d="M3 5l9 8 9-8"/></svg></span>
        <span class="icon-dot"><svg width="12" height="12" viewBox="0 0 24 24" fill="none" stroke="#fff" stroke-width="2"><circle cx="12" cy="12" r="9"/><path d="M3 12h18M12 3c3 3 3 15 0 18M12 3c-3 3-3 15 0 18"/></svg></span>
      </div>
      <p class="contact-line">(+371) 60 555 010</p>
      <p class="contact-line">info@kemsu.lv</p>
      <p class="contact-line">www.kemsu.lv</p>
    </div>
    <div class="back__worker" role="img" aria-label="Photo of a warehouse worker in hard hat and safety vest holding paper rolls"></div>
  </div>

  <div class="page page--front">
    <div class="front__photo" role="img" aria-label="Photo of a bright paper warehouse with stacked white paper pallets"></div>
    <div class="brand front__brand"><span class="brand__mark"></span>KEMSU</div>
    <div class="front__band">
      <h1 class="front__title">WISSENSWERT</h1>
      <p class="front__topics">FORMATE, KLASSEN,<br>FARBEN, BERECHNUNGEN</p>
      <div class="front__rule"></div>
      <p class="front__tagline">Wegweiser für den Umgang mit Papier und Karton</p>
    </div>
    <p class="front__web">www.kemsu.lv</p>
  </div>
</section>

<section class="spread spread--inside">
  <div class="page page--intro">
    <div class="intro__photo" role="img" aria-label="Photo of a smiling man with clipboard beside stacks of coloured paper"></div>
    <svg class="intro__header" viewBox="0 0 420 300" preserveAspectRatio="none" aria-hidden="true">
      <defs><linearGradient id="bandShade" x1="0" x2="1"><stop offset="0" stop-color="#6a1d22"/><stop offset="1" stop-color="#8e3b42"/></linearGradient></defs>
      <path d="M0 0H420V300C300 250 160 225 0 232Z" fill="url(#bandShade)"/>
    </svg>
    <div class="intro__text">
      <h2 class="intro__title">FACHLATEIN FÜR<br>FORTGESCHRITTENE</h2>
      <div class="intro__rule"></div>
      <p class="intro__sub">Die gebräuchlichsten<br>Fachbegriffe und Abkürzungen</p>
    </div>
  </div>

  <div class="page page--glossary">
    <div class="glossary">
      <div class="term term--tile">
        <svg class="term__icon" viewBox="0 0 30 26" fill="none" stroke="#7a2328" stroke-width="1.5"><path d="M3 8l12-5 12 5-12 5z"/><path d="M3 13l12 5 12-5M3 18l12 5 12-5"/></svg>
        <h3 class="term__name">Ungestrichen</h3>
        <p class="term__text">Unveredelte, maschinenglatte oder satinierte Papiere, die aus verschiedenen Faserstoffen hergestellt werden können.</p>
      </div>
      <div class="term">
        <svg class="term__icon" viewBox="0 0 30 26" fill="none" stroke="#7a2328" stroke-width="1.5"><rect x="8" y="3" width="14" height="19"/><path d="M11 8h8M11 11h8M11 14h8M11 17h5"/></svg>
        <h3 class="term__name">Satiniert/<br>scharf satiniert</h3>
        <p class="term__text">In einem Kalander nachträglich und unterschiedlich stark geglättete Papiere.</p>
      </div>
      <div class="term">
        <svg class="term__icon" viewBox="0 0 30 26" fill="none" stroke="#7a2328" stroke-width="1.5"><path d="M8 3h10l5 5v15H8z"/><path d="M18 3v5h5"/></svg>
        <h3 class="term__name">FCO</h3>
        <p class="term__text">In der Papiermaschine (inline) gestrichenes Papier mit matter oder glänzender Oberfläche.</p>
      </div>
      <div class="term term--tile">
        <svg class="term__icon" viewBox="0 0 30 26" fill="none" stroke="#7a2328" stroke-width="1.5"><circle cx="9" cy="9" r="5"/><circle cx="9" cy="9" r="2"/><path d="M14 9v12H24V4H9"/></svg>
        <h3 class="term__name">Matt gestrichen</h3>
        <p class="term__text">Die Oberfläche des Papiers wird in einem zusätzlichen Arbeitsgang mit matten Pigmenten gestrichen.</p>
      </div>
      <div class="term term--tile">
        <svg class="term__icon" viewBox="0 0 30 26" fill="none" stroke="#7a2328" stroke-width="1.5"><path d="M4 18c0-6 4-10 10-10h12v10H4z"/><circle cx="10" cy="15" r="3"/></svg>
        <h3 class="term__name">Halbmatt gestrichen/<br>gestrichen (Silk/Satin)</h3>
        <p class="term__text">Ein besonderer Strichauftrag und/oder spezielles Kalandrieren erzeugen eine halbmatte Oberfläche.</p>
      </div>
      <div class="term">
        <svg class="term__icon" viewBox="0 0 30 26" fill="none" stroke="#7a2328" stroke-width="1.5"><path d="M9 6l2 5 5 2-5 2-2 5-2-5-5-2 5-2zM21 5l1.5 4 4 1.5-4 1.5L21 16l-1.5-4-4-1.5 4-1.5z"/></svg>
        <h3 class="term__name">Glänzend gestrichen</h3>
        <p class="term__text">Durch nachträgliches Satinieren und einen speziellen Strichauftrag entsteht eine glänzende Oberfläche.</p>
      </div>
      <div class="term">
        <svg class="term__icon" viewBox="0 0 30 26" fill="none" stroke="#7a2328" stroke-width="1.5"><rect x="4" y="9" width="22" height="10"/><path d="M9 9V3h12v6M9 16h12v7H9z"/></svg>
        <h3 class="term__name">Gestrichen</h3>
        <p class="term__text">Die Oberfläche des Papiers wird bereits in der Papiermaschine oder nachträglich in einer Streichmaschine durch einen Strichauftrag veredelt. Daraus ergibt sich eine bessere Druckwiedergabe.</p>
      </div>
      <div class="term term--tile">
        <div class="brand"><span class="brand__mark"></span>KEMSU</div>
      </div>
    </div>
  </div>
</section>

</body>
</html>
```